Business Card Design Project

Hello! We need a business card design for a new company opening up in Downtown Dallas called Marbrook Cupcakes. We are a cupcake factory and our primary colors are Harbor Teal and Brown. We want to have a design that can be used for multiple positions (Owner/Operations Manager, Assistant Operations Manager, Decorator, Baker, Corporate Sale Rep, Special Events Rep etc) We would like for it to be double sided. Use the following information in your designs:

Renata Vasquill
Assistant Operations Manager
renata@marbrookcupcakes.example
T555.318.9047

Store Hours:
Mon-Thur 10am-9pm
Fri-Sat 10am-10pm
Sun 12pm-7pm

website: www.marbrookcupcakes.example

Address: 2735 Quarry Ln, Dallas TX 75999

The logo is attached.

Industry/Entity Type

Business

Requirements
Must have
• It must be Harbor Teal and Brown.
Nice to have
• Nice for it to be double sided.
Should not have
• No graphics like a cupcake. Just the word logo.

```html
<!DOCTYPE html>
<html lang="en">
<head>
<meta charset="utf-8">
<title>Marbrook Cupcakes – Business Card</title>
<link rel="stylesheet" href="https://fonts.googleapis.com/css2?family=Lato:wght@400&display=swap">
<style>
  :root {
    --harbor-teal: #6cc3cb;
    --teal-text: #5bb8c2;
    --cocoa: #4a2a22;
    --paper: #fbfbfb;
    --backdrop: #e9e9e9;
  }
  * { box-sizing: border-box; margin: 0; padding: 0; }
  html, body {
    width: 1200px; height: 900px; overflow: hidden;
    background: var(--backdrop);
    font-family: "Lato", sans-serif;
    font-weight: 400;
  }
  .stage {
    width: 1200px; height: 900px;
    display: flex; flex-direction: column; align-items: center; justify-content: center;
    gap: 40px;
  }
  .card {
    width: 700px; height: 400px;
    background: var(--harbor-teal);
    border-radius: 4px;
    position: relative;
    box-shadow: 0 6px 18px rgba(0,0,0,0.12);
  }
  /* Front */
  .card-front .frame {
    position: absolute; inset: 20px;
    border: 1.5px solid var(--cocoa);
    border-radius: 14px;
    display: flex; align-items: center; justify-content: center;
  }
  .wordmark {
    color: #ffffff;
    font-size: 62px;
    letter-spacing: 1px;
  }
  /* Back */
  .card-back .panel {
    position: absolute; inset: 22px;
    background: var(--paper);
    border: 1.5px solid var(--cocoa);
    border-radius: 18px;
  }
  .contact {
    position: absolute; top: 44px; left: 30px; width: 300px;
    text-align: right; color: var(--cocoa);
  }
  .contact .name { color: var(--teal-text); font-size: 22px; }
  .contact .role { font-size: 15px; margin-top: 4px; }
  .contact .lines { font-size: 16px; margin-top: 28px; line-height: 1.45; }
  .contact .address { font-size: 16px; margin-top: 26px; line-height: 1.45; }
  .label { color: var(--teal-text); }
  .divider {
    position: absolute; top: 40px; bottom: 70px; left: 350px;
    border-left: 2px dotted var(--cocoa);
  }
  .hours {
    position: absolute; top: 72px; left: 378px; color: var(--cocoa);
  }
  .hours h2 {
    font-weight: 400; font-size: 19px; letter-spacing: 0.5px;
    color: var(--teal-text); margin-bottom: 6px;
  }
  .hours dl {
    display: grid; grid-template-columns: 110px auto;
    font-size: 18px; line-height: 1.3;
  }
  .hours dd { margin: 0; }
  .back-wordmark {
    position: absolute; right: 36px; bottom: 26px;
    color: var(--teal-text); font-size: 34px;
  }
</style>
</head>
<body>
<main class="stage">
  <section class="card card-front" aria-label="Card front">
    <div class="frame">
      <span class="wordmark">Marbrook Cupcakes</span>
    </div>
  </section>

  <section class="card card-back" aria-label="Card back">
    <div class="panel">
      <div class="contact">
        <p class="name">Renata Vasquill</p>
        <p class="role">Assistant Operations Manager</p>
        <p class="lines">
          <span class="label">t</span>: 555.318.9047<br>
          <span class="label">e</span>: renata@marbrookcupcakes.example
        </p>
        <p class="address">
          2735 Quarry Ln, Dallas TX 75999<br>
          www.marbrookcupcakes.example
        </p>
      </div>
      <div class="divider"></div>
      <div class="hours">
        <h2>STORE HOURS:</h2>
        <dl>
          <dt>Mon-Thur</dt><dd>10am-9pm</dd>
          <dt>Fri-Sat</dt><dd>10am-10pm</dd>
          <dt>Sun</dt><dd>12pm-7pm</dd>
        </dl>
      </div>
      <span class="back-wordmark">Marbrook</span>
    </div>
  </section>
</main>
</body>
</html>
```